Modernise Business Card

Our company has been operating for 10 years. With the start of the new decade we are looking to refresh our business card design. We manufacture a range of industrial product shipping to customers internationally. A copy of our current card, both sides, is attached. We are looking for a mature professional appearance.

```html
<!DOCTYPE html>
<html lang="en">
<head>
<meta charset="utf-8">
<title>Korvane Business Card</title>
<link href="https://fonts.googleapis.com/css2?family=Montserrat:wght@400;500;700&display=swap" rel="stylesheet">
<style>
:root{
  --accent:#00b1de;
  --ink:#111111;
  --ink-soft:#1e1e1e;
  --paper:#ffffff;
  --stage:#d9d9d9;
  --dark-1:#333132;
  --dark-2:#070707;
  --rule:#8a8a8a;
}
*{margin:0;padding:0;box-sizing:border-box}
html,body{width:1200px;height:720px;overflow:hidden}
body{background:var(--stage);position:relative;font-family:'Montserrat',Arial,sans-serif}
.card{position:absolute;width:505px;height:288px;overflow:hidden}
.card-front{left:69px;top:68px}
.card-back{left:645px;top:357px;background:var(--paper)}
.front-texture{position:absolute;inset:0;background:radial-gradient(ellipse at 50% 35%,var(--dark-1) 0%,#1a1a1a 55%,var(--dark-2) 100%)}
.edge-bar{position:absolute;top:43px;width:11px;height:204px;background:var(--accent)}
.edge-bar.left{left:0;clip-path:polygon(0 0,100% 6%,100% 94%,0 100%)}
.edge-bar.right{right:0;clip-path:polygon(0 6%,100% 0,100% 100%,0 94%)}
.front-content{position:absolute;inset:0;display:flex;flex-direction:column;align-items:center;color:var(--paper)}
.brand-name{margin-top:78px;font-weight:700;font-size:52px;letter-spacing:1px;color:var(--accent);line-height:1}
.product-list{margin-top:30px;list-style:none;text-align:center;font-weight:500;font-size:14.5px;line-height:20px;letter-spacing:.2px}
.front-web{margin-top:20px;font-size:13.5px;letter-spacing:.3px}
.back-brand-panel{position:absolute;left:0;top:0;width:221px;height:100%;background:linear-gradient(135deg,#f4f4f4 0%,#ffffff 45%,#f1f1f1 70%,#ffffff 100%)}
.back-brand-panel .brand-name{position:absolute;left:0;right:0;top:117px;margin:0;text-align:center;font-size:36px}
.panel-divider{position:absolute;left:221px;top:0;width:2px;height:100%;background:var(--rule)}
.contact-list{position:absolute;left:228px;top:0;width:260px;list-style:none}
.contact-item{position:absolute;left:0;display:flex;align-items:flex-start;gap:13px;font-size:11px;line-height:14.5px;color:var(--ink-soft);width:262px}
.icon-tile{flex:none;width:22px;height:22px;border-radius:3px;background:var(--accent);display:flex;align-items:center;justify-content:center}
.icon-tile svg{width:15px;height:15px}
.person-name{font-size:31px;font-weight:500;color:var(--ink);line-height:1;white-space:nowrap}
.person-name .surname{color:var(--accent)}
</style>
</head>
<body>

<section class="card card-front">
  <div class="front-texture" role="img" aria-label="Dark charcoal background with soft layered diamond pattern"></div>
  <div class="edge-bar left"></div>
  <div class="edge-bar right"></div>
  <div class="front-content">
    <div class="brand-name">Korvane</div>
    <ul class="product-list">
      <li>HYDRAULIC ADAPTERS</li>
      <li>HOSE FITTINGS</li>
      <li>QUICK COUPLINGS</li>
    </ul>
    <div class="front-web">www.korvanefittings.com</div>
  </div>
</section>

<section class="card card-back">
  <div class="back-brand-panel" role="img" aria-label="Light grey layered diamond pattern behind company name">
    <div class="brand-name">Korvane</div>
  </div>
  <div class="edge-bar left"></div>
  <div class="edge-bar right"></div>
  <div class="panel-divider"></div>

  <ul class="contact-list">
    <li class="contact-item" style="top:41px;align-items:center">
      <span class="icon-tile"><svg viewBox="0 0 16 16"><circle cx="8" cy="5" r="3" fill="#fff"/><path d="M2.5 15c0-3.5 2.5-5.5 5.5-5.5s5.5 2 5.5 5.5z" fill="#fff"/></svg></span>
      <span class="person-name">Ellis <span class="surname">Marran</span></span>
    </li>
    <li class="contact-item" style="top:95px">
      <span class="icon-tile"><svg viewBox="0 0 16 16"><path d="M4 1.5l2.2 3-1.4 1.6c.8 1.8 2.3 3.3 4.1 4.1l1.6-1.4 3 2.2-1.2 2.6C7 13.5 2.5 9 1.4 2.7z" fill="#fff"/></svg></span>
      <span>China: +86 100 5550 0147<br>Australia: +61 400 555 019</span>
    </li>
    <li class="contact-item" style="top:140px;align-items:center">
      <span class="icon-tile"><svg viewBox="0 0 16 16"><rect x="1.5" y="3.5" width="13" height="9" rx="1" fill="none" stroke="#fff" stroke-width="1.5"/><path d="M2 4.5l6 4.5 6-4.5" fill="none" stroke="#fff" stroke-width="1.5"/></svg></span>
      <span>emarran@korvanefittings.com</span>
    </li>
    <li class="contact-item" style="top:177px;align-items:center">
      <span class="icon-tile"><svg viewBox="0 0 16 16" fill="none" stroke="#fff" stroke-width="1.2"><circle cx="8" cy="8" r="6.3"/><ellipse cx="8" cy="8" rx="2.8" ry="6.3"/><path d="M1.7 8h12.6M2.8 4.8h10.4M2.8 11.2h10.4"/></svg></span>
      <span>www.korvanefittings.com</span>
    </li>
    <li class="contact-item" style="top:213px">
      <span class="icon-tile" style="margin-top:8px"><svg viewBox="0 0 16 16"><path d="M8 1.8L1 8h2v6.5h4v-4h2v4h4V8h2z" fill="#fff"/></svg></span>
      <span>88-1,Lanfeng Tower 412 Qiaoxin Road,Haishu District Ningbo 315000 China</span>
    </li>
  </ul>
</section>

</body>
</html>
```